Velvet Stomp Ball Poster

We need a poster design for a local event we are holding in our town. The band playing is called "Tinsel" and the theme is "Glam Rock". We would like to see a design that ties in with the Glam Rock theme and it should be very eyecatching. I have attached a file showing the type of look that you might think is suitable but I am open to suggestions! Thanks so much - I am looking forward to seeing your ideas!!

It also needs to say on the poster that the event is sponsored by the Wandoola CRC (see attached logo) and the Wandoola Progress Association (see attached logo)

Industry/Entity Type

Town

Requirements
Must have
• Must have the following wording...

Calling all Rockers...
The Wandoola Progress Association proudly presents live music by
"Tinsel"
Friday 26th October
7:30pm
Wandoola Hall
Tickets $20 - Available from the Wandoola CRC
Dress - GLAM ROCK

```html
<!DOCTYPE html>
<html lang="en">
<head>
<meta charset="utf-8">
<title>Velvet Stomp Ball – Tinsel Live at Wandoola Hall</title>
<link rel="stylesheet" href="https://fonts.googleapis.com/css2?family=Playfair+Display:wght@500;700&family=Oswald:wght@600&family=Sigmar+One&display=swap">
<style>
  :root {
    --bg-deep: #0c2325;
    --bg-mid: #123437;
    --smoke: #1f6d72;
    --smoke-light: #2f9ea3;
    --slate: #8da6ad;
    --orange: #e7883c;
    --ice: #bfeef0;
    --ice-glow: #3fd6dc;
    --rule: #a9bcc0;
    --white: #ffffff;
    --ink: #3a3a3a;
  }
  * { margin: 0; padding: 0; box-sizing: border-box; }
  html, body { width: 849px; height: 1200px; overflow: hidden; background: var(--bg-deep); }
  .poster {
    position: relative;
    width: 849px;
    height: 1200px;
    overflow: hidden;
    background: radial-gradient(ellipse at 60% 60%, var(--bg-mid), var(--bg-deep) 75%);
    font-family: "Playfair Display", Georgia, serif;
    color: var(--slate);
  }
  .backdrop { position: absolute; inset: 0; }
  .headline {
    position: absolute; top: 148px; left: 0; width: 100%;
    text-align: center; font-size: 60px; font-weight: 700; letter-spacing: 1px;
  }
  .accent { color: var(--orange); }
  .presenter {
    position: absolute; top: 230px; left: 0; width: 100%;
    text-align: center; font-size: 22px; font-weight: 700;
  }
  .lead-in {
    position: absolute; top: 280px; left: 0; width: 100%;
    text-align: center; font-size: 29px; font-weight: 700; color: var(--orange);
  }
  .band-name {
    position: absolute; top: 318px; left: 0; width: 100%;
    text-align: center; font-family: "Sigmar One", Impact, sans-serif;
    font-size: 170px; line-height: 1; color: var(--ice);
    text-shadow: 0 0 14px var(--ice-glow), 0 6px 24px rgba(63,214,220,.55);
  }
  .date {
    position: absolute; left: 90px; top: 555px; font-size: 45px; font-weight: 700; line-height: 1.4;
  }
  .venue {
    font-family: "Oswald", "Arial Narrow", sans-serif; font-weight: 600;
    font-size: 46px; letter-spacing: 1px; margin-left: 14px;
  }
  .rule {
    position: absolute; left: 90px; width: 680px;
    border-top: 2px dotted var(--rule); opacity: .8;
  }
  .rule-1 { top: 716px; }
  .rule-2 { top: 886px; }
  .rule-3 { top: 1040px; }
  .info-label {
    position: absolute; left: 90px; font-size: 42px; font-weight: 700; color: var(--orange);
  }
  .tickets-label { top: 752px; }
  .tickets-detail {
    position: absolute; left: 90px; top: 815px; font-size: 34px; font-weight: 500; letter-spacing: 2px;
  }
  .dress-label { top: 905px; }
  .dress-detail {
    position: absolute; left: 95px; top: 965px; font-size: 35px; font-weight: 500; letter-spacing: 2px;
  }
  .rockers-figures {
    position: absolute; left: 600px; top: 895px; width: 145px; height: 140px;
  }
  .sponsor-strip {
    position: absolute; left: 88px; top: 1070px; width: 390px; height: 103px;
    background: var(--white); display: flex; align-items: center; justify-content: space-around;
    padding: 0 14px; color: var(--ink);
  }
  .sponsor {
    display: flex; align-items: center; gap: 8px;
    font-family: "Oswald", "Arial Narrow", sans-serif; font-weight: 600;
    font-size: 17px; line-height: 1.15; text-transform: uppercase;
  }
  .sponsor-mark { width: 14px; height: 14px; background: var(--orange); flex: none; }
  .sponsor-mark.round { border-radius: 50%; background: var(--smoke); }
</style>
</head>
<body>
  <main class="poster">
    <svg class="backdrop" width="849" height="1200" viewBox="0 0 849 1200" aria-hidden="true">
      <defs>
        <linearGradient id="smoke-fill" x1="0" y1="0" x2="1" y2="1">
          <stop offset="0" stop-color="var(--smoke-light)" stop-opacity=".75"/>
          <stop offset=".5" stop-color="var(--smoke)" stop-opacity=".55"/>
          <stop offset="1" stop-color="var(--bg-mid)" stop-opacity=".2"/>
        </linearGradient>
      </defs>
      <polygon points="0,0 849,0 849,55 0,385" fill="url(#smoke-fill)"/>
      <polygon points="445,0 849,0 849,55 395,135 115,135" fill="var(--bg-deep)" opacity=".55"/>
    </svg>

    <h1 class="headline">Calling all <span class="accent">Rockers...</span></h1>
    <p class="presenter">The Wandoola Progress Association proudly presents</p>
    <p class="lead-in">live music by</p>
    <h2 class="band-name">Tinsel</h2>

    <p class="date">Friday 26th October<br>7:30pm<span class="venue">WANDOOLA HALL</span></p>

    <div class="rule rule-1"></div>
    <p class="info-label tickets-label">Tickets $20</p>
    <p class="tickets-detail">Available from the Wandoola CRC</p>

    <div class="rule rule-2"></div>
    <p class="info-label dress-label">Dress</p>
    <p class="dress-detail">GLAM ROCK</p>
    <svg class="rockers-figures" viewBox="0 0 145 140" role="img" aria-label="Silhouettes of three glam rockers posing">
      <rect width="145" height="140" rx="6" fill="var(--orange)" opacity=".85"/>
    </svg>

    <div class="rule rule-3"></div>
    <footer class="sponsor-strip">
      <div class="sponsor"><span class="sponsor-mark"></span>Wandoola</div>
      <div class="sponsor"><span class="sponsor-mark round"></span>Wandoola Community<br>Resource Centre</div>
    </footer>
  </main>
</body>
</html>
```